Skylantern Save the date / Invitation Card

I need a save the date card (4.25" X 5.5") that will be used to let possible attendees know about an upcoming charity Gala. The organization is Brimvera and can be viewed at brimvera.org. The organization raises money at this event to sponsor clean water projects around the world. The event is held at an upscale hotel in downtown pittsburgh with a catered dinner, dancing, entertainment, music and awards presentations. I also need a folded invitation (7" x 10" pre fold) for for the same event which should match the concept of the save the date card. The concept for both should be classy, eye catching and compliment our branding while not just reusing current assets from the website brimvera.org. I want something that identifies a high class event with a creativity that is eyecatching and memorable.

Target Market(s)

Donors for a high end charity event.

Industry/Entity Type

Charity

Font styles to use
Decorative

Colors

Designer to choose colors to be used in the design.

Requirements
Must have
• The Brimvera logo, the term skylantern,
Nice to have
• I would like to have something a bit darker with pops of bright colors.

```html
<!DOCTYPE html>
<html lang="en">
<head>
<meta charset="utf-8">
<title>Skylantern – Save the Date</title>
<link rel="stylesheet" href="https://fonts.googleapis.com/css2?family=Poiret+One&family=Cormorant+SC:wght@500&family=Cinzel:wght@400&family=Roboto+Condensed:wght@700&display=swap">
<style>
  :root {
    --ink: #07091a;
    --ink-edge: #0d1028;
    --white: #f2f1f6;
    --lavender: #b9a8ef;
    --yellow: #f5c04a;
    --orange: #f2632f;
    --pink: #e2369a;
    --violet: #a04fe0;
    --blue: #4d6ff0;
    --pale: #dcdcf6;
    --brand-blue: #2d7fd0;
  }
  * { margin: 0; padding: 0; box-sizing: border-box; }
  html, body { width: 927px; height: 1200px; overflow: hidden; background: var(--ink); }
  .card {
    position: relative;
    width: 927px;
    height: 1200px;
    background: radial-gradient(ellipse at 50% 40%, var(--ink-edge) 0%, var(--ink) 70%);
    color: var(--white);
    text-align: center;
  }
  .wreath {
    position: absolute;
    left: 157px; top: 58px;
    width: 630px; height: 610px;
    border-radius: 50%;
    background: conic-gradient(from 200deg, var(--violet), var(--blue), var(--violet), var(--pink), var(--orange), var(--pink), var(--pale), var(--pale), var(--orange), var(--pink), var(--violet));
    -webkit-mask: radial-gradient(closest-side, transparent 78%, #000 82%, #000 96%, transparent 100%);
            mask: radial-gradient(closest-side, transparent 78%, #000 82%, #000 96%, transparent 100%);
    opacity: .85;
  }
  .headline {
    position: absolute;
    left: 0; right: 0; top: 198px;
    font-family: "Poiret One", sans-serif;
    line-height: 1;
  }
  .headline span { display: block; }
  .headline .save {
    font-size: 148px;
    background: linear-gradient(90deg, var(--orange), var(--pink) 45%, var(--violet));
    -webkit-background-clip: text; background-clip: text; color: transparent;
  }
  .headline .the {
    font-size: 78px; margin-top: -22px; color: var(--white);
  }
  .headline .date {
    font-size: 148px; margin-top: -44px;
    background: linear-gradient(90deg, var(--pale), var(--lavender) 50%, var(--blue));
    -webkit-background-clip: text; background-clip: text; color: transparent;
  }
  .event-name {
    position: absolute; left: 0; right: 0; top: 688px;
    font-family: "Poiret One", sans-serif;
    font-size: 104px; line-height: 1;
    background: linear-gradient(90deg, var(--pale) 18%, var(--yellow) 26%, var(--orange) 38%, var(--pink) 52%, var(--violet) 66%, var(--blue) 82%);
    -webkit-background-clip: text; background-clip: text; color: transparent;
  }
  .event-date {
    position: absolute; left: 0; right: 0; top: 842px;
    font-family: "Cormorant SC", serif;
    font-size: 33px; letter-spacing: .5px; color: var(--white);
  }
  .blurb {
    position: absolute; left: 0; right: 0; top: 902px;
    font-family: "Cormorant SC", serif;
    font-size: 26px; line-height: 33px; color: var(--lavender);
  }
  .brand {
    position: absolute; left: 0; right: 0; top: 1028px;
    display: flex; justify-content: center; align-items: center; gap: 10px;
    font-family: "Roboto Condensed", sans-serif;
    font-size: 44px; font-weight: 700; color: var(--brand-blue); line-height: 1;
  }
  .brand .dot { width: 22px; height: 22px; border-radius: 50%; background: var(--brand-blue); }
  .foundation {
    position: absolute; left: 0; right: 0; top: 1076px;
    font-family: "Roboto Condensed", sans-serif;
    font-size: 13px; font-weight: 700; color: var(--white);
  }
  .website {
    position: absolute; left: 0; right: 0; top: 1118px;
    font-family: "Cinzel", serif;
    font-size: 21px; letter-spacing: 7px; color: var(--pale);
  }
</style>
</head>
<body>
  <main class="card">
    <div class="wreath" role="img" aria-label="Circular wreath of leaves, berries and flowers in orange, pink, violet and white"></div>
    <h1 class="headline">
      <span class="save">Save</span>
      <span class="the">the</span>
      <span class="date">Date</span>
    </h1>
    <h2 class="event-name">Skylantern</h2>
    <p class="event-date">Event Date Goes Here</p>
    <p class="blurb">Lorem Ipsum is simply dummy text of the<br>printing and typesetting industry.</p>
    <div class="brand"><span class="dot"></span><span>Brimvera</span></div>
    <p class="foundation">Elin Marsh Memorial Foundation</p>
    <p class="website">www.brimvera.org</p>
  </main>
</body>
</html>
```